"Principles for action" poster design for inside company

I would like to create a poster in order to make a message from CEO to employees to be clearly.
A size is A3E(landscape) , and I wish you to design 3 messages(principles for action) into one poster.
("Principles for action" is core value for employees to do everything on working in our company.)
I want you to design and place 3 messages as if they have some relations each other in one poster.
Principles for actions are as follows;
(1)Bird's eye view:
(Meaning: Although there are multiple right answers, it is difficult to gain something if you do not have different view from common one. We request you always to compare subjective view and objective view and then aim to have the specific view.)
(2)Agility:
(Meaning: Maximum rapidity is obtained in any case. Rapid accumulation of trivial reply, delivery, and courtesy, and it will lead to overall competitiveness.)
(3)Back to comfort:
(Meaning:Whatever the type of business be, various ideas are generated by employees. Those born in uncomfortable environment, become bad product that are not comfortable. In other words, managers will be asked to keep the comfortable environment.)
(Summary)
Our company always require employees that "First, you grasp the meaning of everything as if having bird's eyes, and do action rapidly. if you do action rapidly, a lot of important things will be appeared, so that you grasp again on bird's eye.
In order to be these situation worked, it must be always required comfortable environment for employees, so that manager have to create and maintain comfortable environment.
-
No need to add the "meanings" of 3 message, but please place 3 message(Bird's eye view, Agility and Back to comfort) into a poster.
We like some desings below, but you don't need to be swayed too much by them. That is to say, we dont like messy design.
http://www.pixelvantor.net/design/58203
http://www.pixelvantor.net/design/47261
http://www.pixelvantor.net/design/39482
http://www.pixelvantor.net/design/2837465/poster-design-by-plume
http://www.pixelvantor.net/design/2837467/poster-design-by-plume
http://www.pixelvantor.net/design/2649031/poster-design-by-mossylantern
-
the attachment file is the logo data of our company. Please place it anywhere in the poster.

```html
<!DOCTYPE html>
<html lang="en">
<head>
<meta charset="utf-8">
<title>Principles for Action — brightquill</title>
<link rel="stylesheet" href="https://fonts.googleapis.com/css2?family=Audiowide&family=Open+Sans:ital,wght@0,400;0,600;1,400&display=swap">
<style>
  :root {
    --frame: #d3d6d8;
    --paper: #ffffff;
    --ink-blue: #1f3a8f;
    --brand-blue: #1e8fd9;
    --title-stroke: #2a55b8;
    --panel-grey: #cdcfd1;
    --band-light: #d9eef9;
    --band-mid: #5cb8e6;
    --sky-pale: #e4f2fb;
    --sky-mid: #7fc0ec;
    --sky-deep: #2f86d6;
  }
  * { box-sizing: border-box; margin: 0; padding: 0; }
  html, body { width: 1200px; height: 848px; overflow: hidden; background: var(--frame); }
  .poster {
    position: relative; width: 1200px; height: 848px;
    background: var(--frame); font-family: "Open Sans", sans-serif;
  }
  .sheet {
    position: absolute; left: 20px; top: 20px; width: 1160px; height: 808px;
    background: var(--paper); overflow: hidden;
  }
  .backdrop {
    position: absolute; left: 0; top: 0; width: 1160px; height: 808px;
    background: linear-gradient(180deg,
      var(--paper) 0%, var(--paper) 46%,
      var(--sky-pale) 54%, var(--sky-mid) 64%,
      var(--sky-deep) 74%, var(--sky-mid) 86%, var(--sky-deep) 100%);
  }
  .white-band {
    position: absolute; left: 0; top: 708px; width: 1160px; height: 44px; background: var(--paper);
  }
  .brand {
    position: absolute; right: 48px; top: 56px;
    font-weight: 600; font-size: 44px;
    color: var(--brand-blue); letter-spacing: -0.5px;
  }
  .headline {
    position: absolute; left: 0; top: 260px; width: 1160px; text-align: center;
    font-family: "Audiowide", sans-serif; font-weight: 400; font-size: 50px; letter-spacing: 6px;
    color: #eef3fb; -webkit-text-stroke: 2px var(--title-stroke);
    text-shadow: 3px 3px 4px rgba(0,0,0,0.35);
  }
  .principle {
    position: absolute; top: 433px; width: 302px; height: 359px;
    background: var(--paper); border-radius: 14px;
  }
  .principle--specific { left: 80px; }
  .principle--competitive { left: 432px; }
  .principle--relaxed { left: 782px; }
  .principle__title {
    height: 38px; text-align: center; font-style: italic; font-weight: 400; font-size: 30px;
    line-height: 38px; color: var(--ink-blue);
  }
  .principle__panel {
    position: absolute; left: 0; top: 34px; width: 302px; height: 325px;
    background: var(--panel-grey); border-radius: 14px;
  }
  .principle__visual {
    position: absolute; left: 46px; top: 28px; width: 210px; height: 108px; border-radius: 2px;
  }
  .visual--balance { background: linear-gradient(90deg, #b8212a 0 30%, var(--panel-grey) 30% 70%, #f39a1c 70%); opacity: .85; }
  .visual--gauge { background: linear-gradient(135deg, #1b1d22, #3a3e46 60%, #0e1014); box-shadow: 0 2px 5px rgba(0,0,0,.4); }
  .visual--smiles { background: linear-gradient(135deg, #f2d22a, #e8462b 35%, #3bb44a 65%, #2e7ed6); box-shadow: 0 2px 5px rgba(0,0,0,.3); }
  .principle__text {
    position: absolute; left: 0; top: 164px; width: 302px; text-align: center;
    font-style: italic; font-weight: 400; font-size: 20px; line-height: 29px; color: var(--ink-blue);
  }
  .principle__label {
    position: absolute; left: 0; top: 243px; width: 302px; height: 43px;
    background: linear-gradient(90deg, var(--band-light), var(--band-mid) 50%, var(--band-light));
    color: #ffffff; text-align: center; font-weight: 400; font-size: 24px; line-height: 43px;
    text-shadow: 0 0 3px rgba(30,90,160,.5);
  }
</style>
</head>
<body>
<div class="poster">
  <div class="sheet">
    <div class="backdrop" role="img" aria-label="Decorative flowing blue wave artwork"></div>
    <div class="white-band"></div>

    <div class="brand">brightquill</div>

    <h1 class="headline">PRINCIPLES FOR ACTION</h1>

    <section class="principle principle--specific">
      <h2 class="principle__title">Be Specific</h2>
      <div class="principle__panel">
        <div class="principle__visual visual--balance" role="img" aria-label="Photo of an apple and an orange balanced on a scale"></div>
        <p class="principle__text">Compare subjective view<br>and objective view</p>
        <div class="principle__label">BIRD'S EYE VIEW</div>
      </div>
    </section>

    <section class="principle principle--competitive">
      <h2 class="principle__title">Be Competitive</h2>
      <div class="principle__panel">
        <div class="principle__visual visual--gauge" role="img" aria-label="Photo of a speedometer at high speed"></div>
        <p class="principle__text">Trivial reply, delivery,<br>and courtesy</p>
        <div class="principle__label">AGILITY</div>
      </div>
    </section>

    <section class="principle principle--relaxed">
      <h2 class="principle__title">Be Relaxed</h2>
      <div class="principle__panel">
        <div class="principle__visual visual--smiles" role="img" aria-label="Photo of many colourful stress balls"></div>
        <p class="principle__text">Comfortable environment<br>for every employee</p>
        <div class="principle__label">BACK TO COMFORT</div>
      </div>
    </section>
  </div>
</div>
</body>
</html>
```